New Alcoholic Spiked Seltzer Line

We need a can design for a line of low calorie alcoholic seltzer. This product is a sparkling water and vodka drink with no sugar added in a slim 12 oz can.

This is a lighter, healthier, alternative to the sugary ready-to-drinks on the market. The product contains only 3 ingredients: Vodka, Water and Natural Flavors. It has only 100 calories but still has 5% alcohol, so you don't need to sacrifice alcohol to cut calories.

This product also does not contain any preservatives.

We want this design to communicate the following objectives to the consumer and in this order:

1. Appetizing product
2.Low calorie
3.Communicate the type of beverage (Spiked Seltzer)

The brand name of the product is VELKA.

The flavor of the product needed to be used for the design is Mango-Orange.

Comparable products are:

www.brisavelfizz.example/
https://www.tarnowbubble.example
https://quellrind.example/

The designs should not infringe or copy the creative directions of the products mentionned above. They are only given so that you can better understand the type of product we are developing.

Target Market(s)

Young Professional women between the ages of 25 and 44

Industry/Entity Type

Product

Colors

Designer to choose colors to be used in the design.

Requirements
Must have
• Design extendibility, meaning it can be adapted for other flavors.
• This is a new category in the market we are targeting, so consumers must easily be able to identify what type of product this is.

```html
<!DOCTYPE html>
<html lang="en">
<head>
<meta charset="utf-8">
<title>VELKA Spiked Seltzer – Mango-Orange Can Label</title>
<link rel="stylesheet" href="https://fonts.googleapis.com/css2?family=Quicksand:wght@400&family=Roboto:ital,wght@0,400;0,700;0,900;1,500;1,700&display=swap">
<style>
  :root {
    --label-white: #ffffff;
    --band-orange: #f26a1b;
    --band-orange-light: #f9a56b;
    --peach-light: #fdf3e4;
    --peach-mid: #f8d7a8;
    --juice-yellow: #fbb52a;
    --juice-orange: #f5821f;
    --mango-red: #e8493a;
    --mango-green: #9cc24a;
    --brand-blue: #2a8fd3;
    --badge-blue: #1f6fc0;
    --ink-blue: #1d3f8f;
    --page-bg: #eef0f2;
  }
  * { margin: 0; padding: 0; box-sizing: border-box; }
  html, body {
    width: 1200px;
    height: 2800px;
    overflow: hidden;
    background: var(--page-bg);
  }
  .can-label {
    position: relative;
    width: 1200px;
    height: 2800px;
    background: var(--label-white);
    overflow: hidden;
    font-family: "Roboto", Arial, sans-serif;
  }
  .flavor-panel {
    position: absolute;
    left: 0; top: 500px;
    width: 1200px; height: 1480px;
    background: linear-gradient(180deg, var(--peach-light) 0%, var(--peach-mid) 50%, var(--peach-light) 100%);
  }
  .band-horizontal {
    position: absolute;
    left: 0; width: 1200px;
    background: var(--band-orange);
    border-top: 10px solid var(--band-orange-light);
    border-bottom: 10px solid var(--band-orange-light);
  }
  .band-top { top: 380px; height: 48px; }
  .band-bottom { top: 1980px; height: 56px; }
  .band-vertical {
    position: absolute;
    left: 168px; top: 0;
    width: 144px; height: 2036px;
    background: var(--band-orange);
    border-left: 12px solid var(--band-orange-light);
    border-right: 12px solid var(--band-orange-light);
  }
  .flavor-name {
    position: absolute;
    left: 240px; top: 500px;
    transform: translate(-50%, -50%) rotate(-90deg);
    white-space: nowrap;
    color: var(--label-white);
    font-weight: 900;
    font-size: 80px;
    letter-spacing: 10px;
  }
  .brand-name {
    position: absolute;
    left: 380px; top: 60px;
    font-family: "Quicksand", Arial, sans-serif;
    font-weight: 400;
    font-size: 210px;
    line-height: 1;
    letter-spacing: 6px;
    color: var(--brand-blue);
  }
  .product-type {
    position: absolute;
    left: 520px; top: 290px;
    font-style: italic;
    font-weight: 500;
    font-size: 66px;
    color: var(--brand-blue);
  }
  .calorie-badge {
    position: absolute;
    left: 860px; top: 560px;
    width: 300px; height: 300px;
    border-radius: 50%;
    background: var(--badge-blue);
    border: 10px solid var(--label-white);
    box-shadow: 0 0 0 4px var(--badge-blue);
    color: var(--label-white);
    text-align: center;
    display: flex; flex-direction: column; justify-content: center;
  }
  .calorie-badge .badge-lead { font-weight: 700; font-size: 72px; line-height: 1.05; }
  .calorie-badge .badge-value { font-weight: 700; font-size: 48px; line-height: 1.2; }
  .fruit-artwork {
    position: absolute;
    left: 110px; top: 980px;
    width: 960px; height: 820px;
  }
  .ingredients {
    position: absolute;
    left: 340px; top: 2110px;
    color: var(--ink-blue);
  }
  .ingredients-title {
    font-style: italic;
    font-weight: 700;
    font-size: 58px;
    color: var(--badge-blue);
    text-decoration: underline;
    text-decoration-thickness: 5px;
    text-underline-offset: 8px;
    margin-bottom: 24px;
  }
  .ingredients-list {
    font-weight: 400;
    font-size: 50px;
    line-height: 1.3;
  }
</style>
</head>
<body>
  <main class="can-label">
    <div class="flavor-panel"></div>

    <div class="band-vertical"></div>
    <div class="band-horizontal band-top"></div>
    <div class="band-horizontal band-bottom"></div>

    <div class="flavor-name">MANGO-ORANGE</div>

    <svg class="fruit-artwork" viewBox="0 0 960 820" role="img" aria-label="Orange juice splash with halved and whole oranges and sliced fresh mango">
      <defs>
        <linearGradient id="fruitTones" x1="0" y1="0" x2="1" y2="1">
          <stop offset="0%" stop-color="#fbc766"/>
          <stop offset="35%" stop-color="#fbb52a"/>
          <stop offset="65%" stop-color="#f5821f"/>
          <stop offset="88%" stop-color="#e8493a"/>
          <stop offset="100%" stop-color="#f3a13a"/>
        </linearGradient>
      </defs>
      <path d="M60 330 C40 180 200 60 380 90 C520 20 700 90 760 220 C900 260 950 420 900 560 C860 700 700 780 520 760 C360 800 180 740 110 610 C40 520 70 420 60 330 Z" fill="url(#fruitTones)"/>
    </svg>

    <h1 class="brand-name">VELKA</h1>
    <p class="product-type">Spiked Seltzer</p>

    <div class="calorie-badge">
      <span class="badge-lead">Only</span>
      <span class="badge-value">100 CAL.</span>
    </div>

    <section class="ingredients">
      <h2 class="ingredients-title">3 INGREDIENTS:</h2>
      <p class="ingredients-list">Vodka (5%alc./vol.),<br>Water &amp; Natural Flavors</p>
    </section>
  </main>
</body>
</html>
```